Breezeline Climate Crew WA Truck

I want a truck desing that screams Professional, Friendly and serious about work. you can find some of our work on our website, facebook and instagram.
https://breezelinecrew.example.com.au/
https://www.instagram.com/bzcrewox/
https://www.facebook.com/profile.php?id=70318825094631

The design needs to include our refrigeration license: AU38452 and electrical License: EC94031
I want the colours to be consistent with my Logo.

Key Notes to be included in the design, I want to let people know we do the following;
- Commercial and Residential
- Repairs, Service and Installation
- Reverse cycle ducted Air Conditioning
- Wall Split Air Conditioning
- Ceiling Cassettes
- Evaporative Air Conditioning
- Cool Rooms
- Display Fridges
- Beer Chillers

```html
<!DOCTYPE html>
<html lang="en">
<head>
<meta charset="utf-8">
<title>Breezeline Climate Crew WA – Truck Box Graphics</title>
<link rel="stylesheet" href="https://fonts.googleapis.com/css2?family=Montserrat:wght@600;700;800&display=swap">
<style>
  :root {
    --canvas-bg: #eef1f4;
    --warm-yellow: #f5b335;
    --warm-orange: #f08a24;
    --warm-red: #e1262b;
    --cool-blue: #1f7cc2;
    --deep-blue: #1b4f8f;
    --navy-text: #14233f;
    --white: #ffffff;
  }
  html, body {
    margin: 0;
    padding: 0;
    width: 1025px;
    height: 1200px;
    overflow: hidden;
    background: var(--canvas-bg);
    font-family: "Montserrat", Arial, sans-serif;
  }
  .artboard {
    position: relative;
    width: 1025px;
    height: 1200px;
  }
  .box-side {
    position: absolute;
    left: 20px;
    width: 985px;
    height: 520px;
    box-shadow: 0 2px 8px rgba(0,0,0,.18);
  }
  .box-side--driver { top: 45px; }
  .box-side--kerb { top: 635px; }
  .band-white { fill: var(--white); }
  .band-blue { fill: var(--cool-blue); }
  .band-yellow { fill: var(--warm-yellow); }
  .band-red { fill: var(--warm-red); }
  .contact-line {
    fill: var(--white);
    font-weight: 700;
    font-size: 21px;
  }
  .service-line {
    fill: var(--navy-text);
    font-weight: 800;
    font-size: 19px;
  }
  .bullet { fill: var(--warm-red); }
  .brand-name {
    fill: var(--warm-orange);
    font-weight: 800;
    font-size: 50px;
    letter-spacing: 1px;
  }
  .brand-dot { fill: var(--cool-blue); }
  .licence-line {
    fill: var(--white);
    font-weight: 700;
    font-size: 20px;
  }
  .social-mark { fill: var(--white); }
</style>
</head>
<body>
<main class="artboard">

  <!-- Driver side panel: services on the right -->
  <svg class="box-side box-side--driver" viewBox="0 0 985 520" xmlns="http://www.w3.org/2000/svg">
    <defs>
      <linearGradient id="warmSkyDriver" x1="0" y1="0" x2="1" y2="0">
        <stop offset="0" stop-color="#f5b335"/>
        <stop offset="0.55" stop-color="#f08a24"/>
        <stop offset="1" stop-color="#e1262b"/>
      </linearGradient>
    </defs>
    <rect class="band-white" width="985" height="520"/>
    <polygon fill="url(#warmSkyDriver)" points="0,0 985,0 985,104 0,229"/>
    <polygon class="band-blue" points="0,235 985,110 985,122 0,249"/>
    <polygon class="band-blue" points="0,264 300,228 300,239 0,275"/>
    <polygon class="band-yellow" points="0,440 985,355 985,382 0,462"/>
    <polygon class="band-red" points="0,468 985,388 985,402 0,478"/>
    <polygon class="band-blue" points="0,484 985,408 985,520 0,520"/>

    <circle class="brand-dot" cx="95" cy="320" r="16"/>
    <text class="brand-name" x="125" y="305">Breezeline</text>
    <text class="brand-name" x="125" y="360">Climate Crew WA</text>

    <g transform="rotate(-7.2 900 40)">
      <circle class="social-mark" cx="638" cy="33" r="9"/>
      <text class="contact-line" x="654" y="40">bzcrewox</text>
      <rect class="social-mark" x="553" y="57" width="17" height="17" rx="4"/>
      <text class="contact-line" x="578" y="72">profile.php?id=70318825094631</text>
      <text class="contact-line" x="582" y="104">breezelinecrew.example.com.au</text>
    </g>

    <g transform="rotate(-8 955 172)">
      <text class="service-line" x="955" y="172" text-anchor="end">Commercial and Residential <tspan class="bullet">●</tspan></text>
      <text class="service-line" x="955" y="197" text-anchor="end">Repairs, Service and Installation <tspan class="bullet">●</tspan></text>
      <text class="service-line" x="955" y="222" text-anchor="end">Reverse cycle ducted Air Conditioning <tspan class="bullet">●</tspan></text>
      <text class="service-line" x="955" y="247" text-anchor="end">Wall Split Air Conditioning <tspan class="bullet">●</tspan></text>
      <text class="service-line" x="955" y="272" text-anchor="end">Ceiling Cassettes<tspan dx="22">Beer Chillers </tspan><tspan class="bullet">●</tspan></text>
      <text class="service-line" x="955" y="297" text-anchor="end">Evaporative Air Conditioning <tspan class="bullet">●</tspan></text>
      <text class="service-line" x="955" y="322" text-anchor="end">Cool Rooms<tspan dx="22">Display Fridges </tspan><tspan class="bullet">●</tspan></text>
    </g>

    <g transform="rotate(-3 470 470)">
      <text class="licence-line" x="470" y="468">refrigeration license: AU38452</text>
      <text class="licence-line" x="470" y="496">electrical License: EC94031</text>
    </g>
  </svg>

  <!-- Kerb side panel: services on the left -->
  <svg class="box-side box-side--kerb" viewBox="0 0 985 520" xmlns="http://www.w3.org/2000/svg">
    <defs>
      <linearGradient id="warmSkyKerb" x1="0" y1="0" x2="1" y2="0">
        <stop offset="0" stop-color="#e1262b"/>
        <stop offset="0.45" stop-color="#f08a24"/>
        <stop offset="1" stop-color="#f5b335"/>
      </linearGradient>
    </defs>
    <rect class="band-white" width="985" height="520"/>
    <polygon fill="url(#warmSkyKerb)" points="0,0 985,0 985,195 0,60"/>
    <polygon class="band-blue" points="0,66 985,200 985,228 0,78"/>
    <polygon class="band-blue" points="685,210 985,246 985,258 685,222"/>
    <polygon class="band-yellow" points="0,355 985,440 985,462 0,382"/>
    <polygon class="band-red" points="0,388 985,468 985,478 0,402"/>
    <polygon class="band-blue" points="0,408 985,484 985,520 0,520"/>

    <g transform="rotate(8 320 30)">
      <circle class="social-mark" cx="222" cy="23" r="9"/>
      <text class="contact-line" x="240" y="30">bzcrewox</text>
      <rect class="social-mark" x="132" y="47" width="17" height="17" rx="4"/>
      <text class="contact-line" x="156" y="63">profile.php?id=70318825094631</text>
      <text class="contact-line" x="156" y="93">breezelinecrew.example.com.au</text>
    </g>

    <g transform="rotate(8 25 125)">
      <text class="service-line" x="25" y="125"><tspan class="bullet">●</tspan> Commercial and Residential</text>
      <text class="service-line" x="25" y="150"><tspan class="bullet">●</tspan> Repairs, Service and Installation</text>
      <text class="service-line" x="25" y="175"><tspan class="bullet">●</tspan> Reverse cycle ducted Air Conditioning</text>
      <text class="service-line" x="25" y="200"><tspan class="bullet">●</tspan> Wall Split Air Conditioning</text>
      <text class="service-line" x="25" y="225"><tspan class="bullet">●</tspan> Ceiling Cassettes <tspan class="bullet">●</tspan> Beer Chillers</text>
      <text class="service-line" x="25" y="250"><tspan class="bullet">●</tspan> Evaporative Air Conditioning</text>
      <text class="service-line" x="25" y="275"><tspan class="bullet">●</tspan> Cool Rooms <tspan class="bullet">●</tspan> Display Fridges</text>
    </g>

    <circle class="brand-dot" cx="440" cy="300" r="16"/>
    <text class="brand-name" x="470" y="285">Breezeline</text>
    <text class="brand-name" x="470" y="340">Climate Crew WA</text>

    <text class="licence-line" x="465" y="505" text-anchor="middle">refrigeration license: AU38452  |  electrical License: EC94031</text>
  </svg>

</main>
</body>
</html>
```